Live Webcasting Host Wants Template/Theme to Jumpstare Ecommerce Site

Please,Please, Please READ ALL OF THE DESCRIPTION. Thank you.

I need a template for a look for my developer to work with in designing an ecommerce site where clients pay a monthly fee for streaming services and video on demand.

I'll need 2 pages designed:
1) public page
2) client log in landing page.

Please use a CMS (WP preferred) as this will allow is for further content to be added after delivery. Please include the pricing text in boxes in slides (pdf) to help fill out you design for the home page.

The attached slides are to give you a general layout of how I envision the pages. Yes I would like the Client page to be tabbed from the side like in the attached slide.

I've attached company logos for use along with the accompanying .psd and .ai files in the zip. Use the colors in logo in site design.

Thank you for your time.
Updates

Please, no designs. This is for a CMS for webpage design like WordPress or Joomla. Thanks. Added Friday, January 13, 2017

Reason: Looking for more designs.

Target Market(s)

Churches, Organizations, Civic Organizations, Government Agencies (State, Local) -BUT don't let this deter your creativity. Decision makers/influencers will be video production and/or IT personnel.

Industry/Entity Type

It Company

Font styles to use
Sans Serif

Colors
f5f5f5
e8e8e8
333333
fece3e
cbcbcb
33a6d7
000000

Requirements
Must have
• Responsive Design
Nice to have
• One Page Design
Should not have
• SHOULD NOT HAVE White overall background but use white in other ways if you like.

```html
<!DOCTYPE html>
<html lang="en">
<head>
<meta charset="utf-8">
<title>Veluma – Pricing</title>
<link href="https://fonts.googleapis.com/css2?family=Montserrat:wght@400;500;600;700&family=Lato:wght@400&display=swap" rel="stylesheet">
<style>
  :root {
    --orange: #f79a21;
    --blue: #33a6d7;
    --dark: #2b2b2b;
    --ink: #1e1e1e;
    --page: #f1eff0;
    --white: #ffffff;
    --footer-text: #a9a9a9;
  }
  * { margin: 0; padding: 0; box-sizing: border-box; }
  html, body { width: 1200px; height: 1022px; overflow: hidden; }
  body {
    position: relative;
    background: var(--page);
    font-family: "Montserrat", sans-serif;
    color: var(--white);
  }
  .hero {
    position: absolute; left: 0; top: 0; width: 1200px; height: 612px;
    background:
      radial-gradient(ellipse 260px 300px at 640px 300px, rgba(96,140,170,.55), transparent 70%),
      linear-gradient(90deg, #6c5a3a 0%, #b8a45c 22%, #c9b98a 40%, #8d6e5c 60%, #9b8a80 78%, #8e9590 100%);
  }
  .site-header {
    position: absolute; left: 60px; top: 10px; width: 1080px; height: 102px;
    background: rgba(255,255,255,.93);
  }
  .brand {
    position: absolute; left: 14px; top: 24px;
    font-weight: 700; font-size: 50px; letter-spacing: -1px;
    color: var(--ink);
    display: flex; align-items: center; gap: 10px;
  }
  .brand-mark { width: 16px; height: 16px; background: var(--orange); }
  .main-nav {
    position: absolute; top: 73px; left: 0;
    font-weight: 500; font-size: 15.5px; color: var(--ink);
  }
  .main-nav a { position: absolute; white-space: nowrap; color: inherit; text-decoration: none; }
  .main-nav .is-active { padding-bottom: 4px; border-bottom: 2px solid var(--orange); }
  .nav-caret { position: absolute; left: 491px; top: 59px; }
  .login-btn {
    position: absolute; left: 967px; top: 12px; width: 90px; height: 40px;
    border: 2px solid var(--orange); border-radius: 2px;
    font-weight: 700; font-size: 16px; color: var(--ink);
    display: flex; align-items: center; justify-content: center; letter-spacing: .5px;
  }
  .plan {
    position: absolute; top: 481px; width: 359px; height: 444px;
    background: var(--blue); border-bottom: 4px solid var(--orange);
  }
  .plan-head { height: 131px; background: var(--orange); text-align: center; }
  .plan-name { padding-top: 12px; font-weight: 600; font-size: 47px; letter-spacing: 2px; }
  .plan-price {
    position: absolute; left: 50%; top: 75px; width: 124px; height: 124px; margin-left: -68px;
    border-radius: 50%; background: var(--dark); border: 3px solid var(--orange);
    display: flex; align-items: center; justify-content: center;
  }
  .price-sign { font-weight: 400; font-size: 62px; line-height: 1; margin-right: 2px; }
  .price-amount { font-weight: 600; font-size: 33px; }
  .plan-row { position: absolute; left: 0; width: 100%; text-align: center; border-top: 1px solid rgba(255,255,255,.35); }
  .plan-hours { top: 233px; height: 81px; padding-top: 14px; }
  .hours-title { font-weight: 600; font-size: 26px; letter-spacing: .5px; }
  .hours-note { font-family: "Lato", sans-serif; font-size: 14px; margin-top: 4px; }
  .plan-storage { top: 314px; padding-top: 26px; }
  .storage-size { font-weight: 600; font-size: 41px; line-height: 1.05; }
  .storage-label { font-weight: 400; font-size: 21px; }
  .site-footer {
    position: absolute; left: 0; top: 972px; width: 1200px; height: 50px;
    background: var(--dark); color: var(--footer-text);
    font-family: "Lato", sans-serif; font-size: 14.5px;
    display: flex; align-items: center; justify-content: center;
  }
</style>
</head>
<body>
  <div class="hero" role="img" aria-label="Photo of a smiling listener wearing headphones outdoors against a brick wall"></div>

  <header class="site-header">
    <div class="brand"><span class="brand-mark"></span>Veluma</div>
    <svg class="nav-caret" width="14" height="9" viewBox="0 0 14 9"><path d="M0 0h14L7 9z" fill="#f79a21"/></svg>
    <nav class="main-nav">
      <a class="is-active" style="left:461px" href="#">FEATURES</a>
      <a style="left:573px" href="#">PRICING</a>
      <a style="left:667px" href="#">ABOUT US</a>
      <a style="left:783px" href="#">WEBCASTING 101</a>
      <a style="left:953px" href="#">CONTACT US</a>
    </nav>
    <a class="login-btn" href="#">LOGIN</a>
  </header>

  <section class="plan" style="left:56px">
    <div class="plan-head"><h2 class="plan-name">SMALL</h2></div>
    <div class="plan-price"><span class="price-sign">$</span><span class="price-amount">49</span></div>
    <div class="plan-row plan-hours"><div class="hours-title">400 VIEWER HOURS</div><div class="hours-note">(50 Viewers watching 2 hrs 4 times per month)</div></div>
    <div class="plan-row plan-storage"><div class="storage-size">100 GB</div><div class="storage-label">Month of video Storage</div></div>
  </section>

  <section class="plan" style="left:420px">
    <div class="plan-head"><h2 class="plan-name">MEDIUM</h2></div>
    <div class="plan-price"><span class="price-sign">$</span><span class="price-amount">399</span></div>
    <div class="plan-row plan-hours"><div class="hours-title">4000 VIEWER HOURS</div><div class="hours-note">(500 Viewers watching 2 hrs 4 times per month)</div></div>
    <div class="plan-row plan-storage"><div class="storage-size">500 GB</div><div class="storage-label">Month of video Storage</div></div>
  </section>

  <section class="plan" style="left:784px">
    <div class="plan-head"><h2 class="plan-name">LARGE</h2></div>
    <div class="plan-price"><span class="price-sign">$</span><span class="price-amount">999</span></div>
    <div class="plan-row plan-hours"><div class="hours-title">16000 VIEWER HOURS</div><div class="hours-note">(2000 Viewers watching 2 hrs 4 times per month)</div></div>
    <div class="plan-row plan-storage"><div class="storage-size">2000 GB</div><div class="storage-label">Month of video Storage</div></div>
  </section>

  <footer class="site-footer">© 2017 Copyright Veluma All Right Reserved</footer>
</body>
</html>
```